Flyer für ambulante und teilstationäre Pflege
Zielgruppe
ambulante und teilstationäre Pflege
Zielgruppe: Pflegebedürftige Menschen, die noch ausreichend mobil sind, um als Gast in unserer Tagespflege zu sein
Aufgabenstellung
Standard DIN lang Format
Stil soll unserer Homepage folgen: www.pflegeteam-sonnhalde.de
Wir achten immer sehr darauf, nicht so einen verstaubten Stil wie viele andere Pflegeeinrichtungen zu haben, sondern fröhlich, bunt , ansprechend

```html
<!DOCTYPE html>
<html lang="de">
<head>
<meta charset="utf-8">
<title>Flyer Pflegeteam Sonnhalde</title>
<link href="https://fonts.googleapis.com/css2?family=Exo+2:wght@400;600;700&family=Montserrat:wght@400;500;700&display=swap" rel="stylesheet">
<style>
:root{
  --teal:#139a8f;
  --red:#8e2027;
  --stage:#747474;
  --paper:#ffffff;
  --soft-grey:#d6d3d5;
  --box-grey:#8b8b8e;
  --box-pink:#c8aabb;
  --ink:#2a2a2a;
}
*{box-sizing:border-box;margin:0;padding:0}
html,body{width:1200px;height:1117px;overflow:hidden}
body{background:var(--stage);position:relative;font-family:"Montserrat",sans-serif;color:var(--ink)}
.page{position:absolute;top:66px;width:493px;height:985px;background:var(--paper);overflow:hidden;box-shadow:0 4px 14px rgba(0,0,0,.35)}
.page--front{left:108px}
.page--back{left:631px}
.topline{position:absolute;top:0;left:0;right:0;height:7px;display:flex}
.topline span:first-child{width:336px;background:var(--teal)}
.topline span:last-child{flex:1;background:var(--red)}
.photo{position:absolute}
/* front header */
.brand{position:absolute;top:28px;display:flex;align-items:center;gap:5px;white-space:nowrap;font-family:"Exo 2",sans-serif;font-weight:600;font-size:12px;color:#4a4a4a}
.brand i{display:block;flex:none;width:28px;height:28px;border-radius:50%}
.brand--care{left:40px}
.brand--care i{background:var(--red)}
.brand--day{left:258px}
.brand--day i{background:var(--teal)}
.hero{left:0;top:76px;width:493px;height:300px;background:linear-gradient(120deg,#7a4a5c 0%,#c8a8b2 45%,#e9e2e0 60%,#6b3e57 100%)}
.headline{position:absolute;top:382px;left:0;width:100%;text-align:center;font-family:"Exo 2",sans-serif;color:var(--teal)}
.headline h1{font-size:38px;font-weight:700;line-height:1.05}
.headline p{font-size:29px;font-weight:400;line-height:1.1}
.tiles{position:absolute;top:474px;left:35px;display:flex;gap:9px}
.tile{width:100px;height:124px;background:#fff;border-radius:0 10px 10px 10px;box-shadow:4px 4px 0 #d9d9d9;text-align:center;padding-top:6px}
.tile .dot{width:84px;height:84px;border-radius:50%;margin:0 auto 10px}
.tile span{font-family:"Exo 2",sans-serif;font-weight:600;font-size:10px;color:var(--teal)}
.lower{position:absolute;left:0;top:622px;width:493px;height:363px;background:var(--soft-grey)}
.room{left:0;top:643px;width:246px;height:256px;background:linear-gradient(160deg,#d9c0cc 0%,#9a6a85 50%,#5c3e58 100%)}
.intro{position:absolute;left:195px;top:661px;width:282px;height:254px;background:#fff;padding:16px 14px 0 21px;box-shadow:-5px 5px 0 #bdbbbd}
.intro h2{font-family:"Exo 2",sans-serif;font-weight:700;font-size:13.5px;line-height:16px;color:var(--red);margin-bottom:5px}
.intro p{font-size:9.3px;line-height:11.4px;margin-bottom:10px}
.cta{position:absolute;display:flex;align-items:center;justify-content:center;background:var(--red);color:#fff;font-family:"Exo 2",sans-serif;font-weight:700;font-size:14px;border-radius:20px;border:2px solid #fff}
.cta--front{left:218px;top:897px;width:236px;height:38px}
.url{position:absolute;left:0;top:947px;width:100%;text-align:center;font-family:"Exo 2",sans-serif;font-weight:700;font-size:13px;color:var(--teal)}
/* back */
.back-title{position:absolute;top:34px;left:0;width:100%;text-align:center;font-family:"Exo 2",sans-serif;font-weight:700;font-size:21px;color:var(--teal)}
.scene{left:0;top:76px;width:493px;height:147px;background:linear-gradient(180deg,#8aa2c0 0%,#b9a98a 55%,#7c8a55 100%)}
.food{left:0;top:223px;width:493px;height:468px;background:linear-gradient(170deg,#a3a179 0%,#e8dcb8 30%,#cfc09a 60%,#4d4a3c 100%)}
.fact{position:absolute;color:#fff}
.fact--grey{background:rgba(132,132,136,.96);left:29px;width:230px;padding:0 40px 0 20px}
.fact--pink{background:rgba(200,170,187,.97);left:234px;width:230px;padding:0 12px 0 20px}
.fact svg{display:block;margin-bottom:10px}
.fact h3{font-family:"Montserrat",sans-serif;font-weight:700;font-size:9px;line-height:11.5px;margin-bottom:5px}
.fact p{font-size:9px;line-height:12px}
.band{position:absolute;left:0;top:691px;width:493px;height:106px;background:var(--teal);color:#fff;text-align:center;font-family:"Exo 2",sans-serif;font-weight:700;font-size:14px;line-height:18px;padding-top:19px}
.cta--back{left:127px;top:775px;width:238px;height:39px;z-index:2}
.bottom{position:absolute;left:0;top:797px;width:493px;height:188px;background:var(--soft-grey)}
.snack{left:0;top:797px;width:267px;height:188px;background:linear-gradient(135deg,#5f86c6 0%,#e9e6e2 45%,#b55a22 75%,#f3f1ee 100%)}
.contact{position:absolute;left:283px;top:823px;font-size:9.6px;line-height:12px}
.contact h4{font-family:"Montserrat",sans-serif;font-weight:700;font-size:10px;margin-bottom:6px}
.row{display:flex;gap:10px;align-items:flex-start;margin-bottom:8px}
.row svg{flex:none}
.row b{color:var(--teal);font-weight:700}
.follow{display:flex;align-items:center;gap:6px;margin-top:12px}
.follow i{display:block;width:12px;height:12px;border-radius:50%;background:var(--teal)}
</style>
</head>
<body>

<section class="page page--front">
  <div class="topline"><span></span><span></span></div>
  <div class="brand brand--care">PFLEGETEAM SONNHALDE <i></i></div>
  <div class="brand brand--day">TAGESPFLEGE AM LINDENHOF <i></i></div>

  <div class="photo hero" role="img" aria-label="Foto: Pflegerin liest mit einer Seniorin lachend aus einem Buch"></div>

  <div class="headline">
    <h1>Von Menschzu Mensch</h1>
    <p>Pflegeprofis seit 1994</p>
  </div>

  <div class="tiles">
    <div class="tile"><div class="dot" role="img" aria-label="Foto: Blutdruckmessung" style="background:radial-gradient(circle,#8a6a7a,#2c2228)"></div><span>Ambulante Pflege</span></div>
    <div class="tile"><div class="dot" role="img" aria-label="Foto: Ballspiel in der Tagespflege" style="background:radial-gradient(circle at 60% 30%,#e0507a,#a4a07c 45%,#e6e3dd)"></div><span>Tagespflege</span></div>
    <div class="tile"><div class="dot" role="img" aria-label="Foto: Leuchtturm-Figur und Muscheln" style="background:radial-gradient(circle,#d8cfc4,#7a5c4e)"></div><span>Über uns</span></div>
    <div class="tile"><div class="dot" role="img" aria-label="Foto: Ausflug an den Strand" style="background:linear-gradient(180deg,#2f6bc4 0%,#7fb0e6 50%,#d6cbb6 70%)"></div><span>Job &amp; Karriere</span></div>
  </div>

  <div class="lower"></div>
  <div class="photo room" role="img" aria-label="Foto: Gäste im Aufenthaltsraum der Tagespflege"></div>
  <article class="intro">
    <h2>Ambulanten Krankenpflege<br>Sonnhalde &amp; Lindenau</h2>
    <p>Seit fast 30 Jahren sind wir nun schon Ihr Experte für häusliche Pflege und Demenzbetreuung. Ihr persönliches Wohl und das Ihrer Angehörigen liegt uns am Herzen, Wir haben es uns zur Herausforderung gemacht, Ihnen in Sachen Pflege bestmögliche Unterstützung anzubieten.</p>
    <p>Nicht nur die Aufgaben, die wir als ambulanter Pflegedienst übernehmen sind vielfältig, sondern auch die Personen die wir betreuen.</p>
    <p>Lassen Sie sich von uns in Ihrem Alltag behilflich sein und machen Sie noch heute einen Beratungstermin zu unseren Dienstleistungen mit einem unserer kompetenten Ansprechpartner.</p>
  </article>
  <div class="cta cta--front">Pflegedienst kontaktieren</div>
  <div class="url">www.pflegeteam-sonnhalde.de</div>
</section>

<section class="page page--back">
  <div class="topline"><span></span><span></span></div>
  <h2 class="back-title">Was unseren Pflegedienst auszeichnet</h2>

  <div class="photo scene" role="img" aria-label="Foto: Senioren mit Betreuerinnen vor dem Kleinbus der Tagespflege"></div>
  <div class="photo food" role="img" aria-label="Foto: Gebäck mit Puderzucker, unscharf im Hintergrund"></div>

  <div class="fact fact--grey" style="top:201px;height:206px;padding-top:16px">
    <svg width="52" height="52" viewBox="0 0 52 52" fill="none" stroke="#fff" stroke-width="2"><circle cx="26" cy="26" r="24"/><circle cx="26" cy="22" r="10"/><path d="M20 30l-4 10 5-2 3 4 2-8M32 30l4 10-5-2-3 4-2-8"/><path d="M26 17l1.5 3 3.3.4-2.4 2.3.6 3.3-3-1.6-3 1.6.6-3.3-2.4-2.3 3.3-.4z" stroke-width="1.2"/></svg>
    <h3>Über 25 Jahre Erfahrung:</h3>
    <p>Über 25 Jahre Erfahrung in der Pflege zahlen sich aus. Wir haben gelernt, was Menschen im Alter wichtig ist und diese Erfahrungen geben wir gerne weiter. Dabei sind uns zufriedene Patienten und Mitarbeiter gleichermaßen wichtig.</p>
  </div>
  <div class="fact fact--pink" style="top:225px;height:207px;padding-top:9px">
    <svg width="52" height="52" viewBox="0 0 52 52" fill="none" stroke="#fff" stroke-width="2"><circle cx="26" cy="26" r="24"/><path d="M19 14h10l5 5v19H19z"/><path d="M29 14v5h5M23 25h8M23 29h8M23 33h8"/></svg>
    <h3>Abgestimmtes Versorgungskonzept mit Beratung zur Finanzierung:</h3>
    <p>Unsere Versorgungskonzepte sind auf all Ihre individuellen Bedürfnisse anpassbar. Wir versuchen stets Ihren Vorstellungen gerecht zu werden und die passende Lösung zu finden. Wir beraten Sie außerdem umfassend zur Finanzierung Ihrer Pflegeleistungen und bieten transparente und nachvollziehbare Kostenaufstellungen.</p>
  </div>
  <div class="fact fact--grey" style="top:445px;height:207px;padding-top:18px;padding-left:18px">
    <svg width="52" height="52" viewBox="0 0 52 52" fill="none" stroke="#fff" stroke-width="2" style="margin-left:4px"><circle cx="26" cy="26" r="24"/><rect x="12" y="21" width="28" height="10" rx="5" transform="rotate(45 26 26)"/><rect x="12" y="21" width="28" height="10" rx="5" transform="rotate(-45 26 26)"/></svg>
    <h3>Sehr gute MDK geprüfte Pflegequalität auf höchstem Niveau:</h3>
    <p>Das von uns erreichte hohe Qualitätsniveau bei der Versorgung Pflegebedürftiger wurde von den Verbänden der Kranken- und Pflegekassen anerkannt und spiegelt sich in den jährlichen sehr guten Benotungen wider.</p>
  </div>
  <div class="fact fact--pink" style="top:469px;height:207px;padding-top:14px">
    <svg width="52" height="52" viewBox="0 0 52 52" fill="none" stroke="#fff" stroke-width="2"><circle cx="26" cy="26" r="24"/><rect x="17" y="18" width="15" height="19" rx="2"/><path d="M19 14h11v4H19M24.5 23v8M20.5 27h8"/><rect x="29" y="30" width="12" height="6" rx="3" transform="rotate(-30 35 33)"/></svg>
    <h3>Zulassung und Versorgungsvertrag mit allen Kranken- und Pflegekassen:</h3>
    <p>Wir haben Versorgungsverträge mit allen Kranken- und Pflegekassen, Sie müssen sich also keine Sorgen machen, die in Anspruch genommenen Pflegeleistungen mit Ihren Kassen abzurechnen. Gerne helfen wir bei Antragstellungen, MDK Begutachtungen und Widersprüchen.</p>
  </div>

  <div class="band">Nirgends sonst in der Region erhalten Sie so hochqualitative<br>und zuverlässige Pflege wie bei uns! Wir helfen Ihnen dabei,<br>Ihr Leben einfacher zu gestalten. Rufen Sie uns an!</div>
  <div class="bottom"></div>
  <div class="cta cta--back">Pflegedienst kontaktieren</div>
  <div class="photo snack" role="img" aria-label="Foto: Weißwurst und Brezel auf blau-weißer Serviette"></div>

  <div class="contact">
    <h4>Tagespflege am Lindenhof</h4>
    <div class="row"><svg width="14" height="14" viewBox="0 0 14 14"><path d="M7 1a4.5 4.5 0 0 1 4.5 4.5C11.5 9 7 13 7 13S2.5 9 2.5 5.5A4.5 4.5 0 0 1 7 1z" fill="#139a8f"/><circle cx="7" cy="5.5" r="1.6" fill="#d6d3d5"/></svg><span>Lindenweg 12<br>24100 Sonnhalde</span></div>
    <div class="row"><svg width="14" height="14" viewBox="0 0 14 14"><circle cx="7" cy="7" r="6.5" fill="#139a8f"/><path d="M4.5 3.8l1.4-.3.8 1.8-.9.7a5 5 0 0 0 2.2 2.2l.7-.9 1.8.8-.3 1.4c-3 .3-6-2.7-5.7-5.7z" fill="#fff"/></svg><span>+49(0)431 12 34 56 70</span></div>
    <div class="row"><svg width="14" height="14" viewBox="0 0 14 14"><circle cx="7" cy="7" r="6.5" fill="#139a8f"/><rect x="3.5" y="4.5" width="7" height="5" fill="none" stroke="#fff" stroke-width="1"/><path d="M3.5 4.5L7 7.5l3.5-3" fill="none" stroke="#fff" stroke-width="1"/></svg><span>info@pflegeteam-sonnhalde.de</span></div>
    <div class="row"><svg width="14" height="14" viewBox="0 0 14 14"><circle cx="7" cy="7" r="6.5" fill="#139a8f"/><g fill="none" stroke="#fff" stroke-width=".9"><circle cx="7" cy="7" r="3.8"/><ellipse cx="7" cy="7" rx="1.6" ry="3.8"/><path d="M3.2 7h7.6"/></g></svg><b>www.pflegeteam-sonnhalde.de</b></div>
    <div class="follow"><span>Follow us on</span><i></i><i></i></div>
  </div>
</section>

</body>
</html>
```